Business card with logo for a family psychologist

I need a business card for my private practice in the urban Chicago area as a psychologist. I see families and individuals who are going through difficult times - divorce, separation, illness, or trauma. I want to project hopefulness, competence, and caring.

Target Market(s)

Adults, other professionals - such as physicans and lawyers

Industry/Entity Type

Health Care

Contact Information for Business Card

Front should have my name and credentials; back should have location information including my email, phone

Font styles to use
Serif
Decorative
Script

Requirements
Must have
• Unique logo
Should not have
• No pictures or icons of people; no black

```html
<!DOCTYPE html>
<html lang="en">
<head>
<meta charset="utf-8">
<title>Business Card – Lakeview Family Psychology</title>
<link rel="stylesheet" href="https://fonts.googleapis.com/css2?family=Lora:wght@400;500;600&display=swap">
<style>
  :root {
    --maroon: #8a1a3c;
    --maroon-deep: #6e0f2c;
    --teal: #1f7f7b;
    --teal-light: #3aa39b;
    --page: #e9e5e0;
    --card-top: #fbfbfb;
    --card-bottom: #eef0f1;
    --text-font: "Lora", Georgia, serif;
  }
  * { margin: 0; padding: 0; box-sizing: border-box; }
  html, body {
    width: 1200px; height: 970px; overflow: hidden;
    background: var(--page);
  }
  .canvas { position: relative; width: 1200px; height: 970px; }
  .card {
    position: absolute; left: 100px; top: 201px;
    width: 1000px; height: 568px;
    border-radius: 24px; overflow: hidden;
    background: linear-gradient(180deg, var(--card-top), var(--card-bottom));
    box-shadow: 0 14px 40px rgba(60, 40, 40, 0.18);
    font-family: var(--text-font);
  }
  .brand {
    position: absolute; left: 40px; top: 110px; width: 420px;
    text-align: center;
  }
  .brand-dot {
    display: block; width: 120px; height: 120px; margin: 0 auto 48px;
    border-radius: 50%; background: var(--teal);
  }
  .brand-name {
    font-size: 38px; font-weight: 500; line-height: 1.15;
    color: var(--maroon);
  }
  .divider {
    position: absolute; left: 493px; top: 115px;
    width: 2px; height: 280px; background: var(--teal);
  }
  .details { position: absolute; left: 534px; top: 118px; }
  .person-name {
    font-size: 35px; font-weight: 500; color: var(--teal);
    letter-spacing: 0.3px;
  }
  .address {
    margin-top: 66px; font-size: 27px; line-height: 37px;
    color: var(--maroon); font-style: normal;
  }
  .contact { margin-top: 20px; list-style: none; }
  .contact li {
    display: flex; align-items: center; gap: 16px;
    font-size: 27px; line-height: 35px; color: var(--maroon);
  }
  .contact svg { width: 30px; height: 30px; flex: none; }
  .wave { position: absolute; left: 0; bottom: 0; width: 1000px; height: 568px; }
</style>
</head>
<body>
<div class="canvas">
  <section class="card">
    <svg class="wave" viewBox="0 0 1000 568" aria-hidden="true">
      <defs>
        <linearGradient id="bandFill" x1="0" x2="1" y1="0" y2="0">
          <stop offset="0" stop-color="#9a2a4a"/>
          <stop offset="1" stop-color="#6e0f2c"/>
        </linearGradient>
      </defs>
      <path d="M0,455 C260,560 620,560 1000,445 L1000,568 L0,568 Z" fill="url(#bandFill)"/>
      <path d="M0,448 C270,548 620,552 1000,438" fill="none" stroke="#d9c7a8" stroke-width="3"/>
      <path d="M10,446 C300,552 650,540 990,432" fill="none" stroke="var(--teal)" stroke-width="9" stroke-linecap="round"/>
    </svg>

    <div class="brand">
      <span class="brand-dot"></span>
      <p class="brand-name">Lakeview Family Psychology</p>
    </div>

    <div class="divider"></div>

    <div class="details">
      <h1 class="person-name">Dana Whitfield, Ph.D.</h1>
      <address class="address">240 W. Lakeside Ave Suite 810<br>Chicago, Illinois 60654</address>
      <ul class="contact">
        <li>
          <svg viewBox="0 0 30 30" aria-hidden="true">
            <rect width="30" height="30" rx="4" fill="var(--teal)"/>
            <path d="M10 7 l3 0 1.5 4.5 -2 1.5 c1 2.5 2.5 4 5 5 l1.5 -2 4.5 1.5 0 3 c-8 1 -14 -5 -13.5 -13.5z" fill="#fff"/>
          </svg>
          <span>312-555-0148</span>
        </li>
        <li>
          <svg viewBox="0 0 30 30" aria-hidden="true">
            <rect width="30" height="30" rx="4" fill="var(--teal)"/>
            <rect x="6" y="9" width="18" height="12" fill="none" stroke="#fff" stroke-width="2"/>
            <path d="M6 9 l9 7 9 -7 M6 21 l7 -6 M24 21 l-7 -6" fill="none" stroke="#fff" stroke-width="1.8"/>
          </svg>
          <span>drdanawhitfield@example.com</span>
        </li>
      </ul>
    </div>
  </section>
</div>
</body>
</html>
```